Home page for our TLR Custodial Legacy Fund

Home page to be created based on photo and information shown attached document.
Viewers will click on either Bienvenue (French) or Welcome (English) to enter the web site.
Refer to following web site for more information on TLR:

http://www.wildlandtrustexample.ca/en/our-sites/east-coast/key-sites/the-harbour-point.html#.QxTrMkp2aZ4

Photo is courtesy of Gary Ostlund and his name should be credited on the web page.

Colors

Designer to choose colors to be used in the design.

```html
<!DOCTYPE html>
<html lang="en">
<head>
<meta charset="utf-8">
<title>TLR Custodial Legacy Fund</title>
<link rel="stylesheet" href="https://fonts.googleapis.com/css2?family=Libre+Baskerville:ital,wght@0,700;1,400;1,700&family=Delius&display=swap">
<style>
  :root {
    --page-bg: #ffffff;
    --marsh-gold: #c9a25a;
    --marsh-light: #d8bd86;
    --autumn-red: #a8352f;
    --forest-green: #3e6b35;
    --river-blue: #b9cde0;
    --tab-white: #f6f6f4;
    --tab-fold: #3a3a3a;
    --ink: #1f1f1f;
    --brand-green: #15933f;
    --button-top: #2ad070;
    --button-bottom: #0b8c3c;
    --button-edge: #0a6a2e;
    --title-veil: rgba(255, 255, 255, 0.55);
    --credit-green: #1a8f3c;
    --rule: #1e5a2c;
  }
  * { box-sizing: border-box; margin: 0; padding: 0; }
  html, body {
    width: 1200px; height: 800px; overflow: hidden;
    background: var(--page-bg);
  }
  .home {
    position: relative; width: 1200px; height: 800px;
  }
  .hero-photo {
    position: absolute; left: 31px; top: 50px; width: 1136px; height: 667px;
    background:
      linear-gradient(180deg, rgba(216,189,134,0.35) 0%, rgba(0,0,0,0) 40%, rgba(60,40,20,0.12) 100%),
      linear-gradient(90deg,
        var(--autumn-red) 0%, var(--forest-green) 14%, #8a7a3e 24%,
        var(--marsh-gold) 34%, var(--marsh-light) 47%, var(--marsh-gold) 58%,
        #b39350 68%, var(--forest-green) 80%, #8d4a36 90%, var(--forest-green) 100%);
  }
  .brand-tab {
    position: absolute; left: 433px; top: 31px; width: 348px; height: 196px;
    background: var(--tab-white);
    clip-path: polygon(0 0, 100% 0, 100% 80%, 50% 100%, 0 80%);
    display: flex; align-items: center; justify-content: center; gap: 14px;
    padding-bottom: 40px;
  }
  .brand-fold {
    position: absolute; left: 413px; top: 31px; width: 0; height: 0;
    border-left: 20px solid transparent;
    border-bottom: 18px solid var(--tab-fold);
  }
  .brand-mark {
    width: 26px; height: 26px; border-radius: 50%; background: var(--brand-green);
    flex: none;
  }
  .brand-name {
    font-family: "Libre Baskerville", Georgia, serif;
    font-weight: 700; font-size: 26px; line-height: 1.15; color: var(--ink);
    text-align: left;
  }
  .fund-title {
    position: absolute; left: 257px; top: 366px; width: 684px; height: 125px;
    background: var(--title-veil);
    border-radius: 6px;
    display: flex; flex-direction: column; justify-content: center; align-items: center;
    font-family: "Libre Baskerville", Georgia, serif;
    font-style: italic; font-weight: 700; font-size: 25px; line-height: 1.75;
    color: #111; text-transform: uppercase;
    text-shadow: 0 1px 2px rgba(255,255,255,0.6);
  }
  .enter-button {
    position: absolute; top: 612px; width: 231px; height: 70px;
    background: linear-gradient(180deg, var(--button-top), var(--button-bottom));
    border-bottom: 4px solid var(--button-edge);
    border-radius: 4px;
    box-shadow: 0 3px 6px rgba(0,0,0,0.35);
    display: flex; align-items: center; justify-content: center;
    font-family: "Libre Baskerville", Georgia, serif;
    font-style: italic; font-size: 27px; color: #ffffff;
    text-decoration: none;
  }
  .enter-button--english { left: 74px; }
  .enter-button--french { left: 895px; }
  .photo-credit {
    position: absolute; left: 31px; top: 748px; width: 1136px; height: 24px;
    display: flex; align-items: center; gap: 14px;
  }
  .photo-credit__rule { flex: 1; height: 1px; background: var(--rule); }
  .photo-credit__dot {
    width: 9px; height: 9px; border-radius: 50%; background: var(--credit-green);
  }
  .photo-credit__text {
    font-family: "Delius", "Comic Sans MS", cursive;
    font-size: 20px; color: var(--credit-green); white-space: nowrap;
  }
</style>
</head>
<body>
  <main class="home">
    <div class="hero-photo" role="img" aria-label="Aerial view of a winding river through golden autumn marshland bordered by red shrubs and evergreen forest"></div>

    <div class="brand-fold"></div>
    <header class="brand-tab">
      <span class="brand-mark"></span>
      <span class="brand-name">Tidal Lands<br>Reserve</span>
    </header>

    <h1 class="fund-title">
      <span>Font de dotation de l’intendance RTL/</span>
      <span>TLR Custodial Legacy Fund</span>
    </h1>

    <a class="enter-button enter-button--english" href="#en" lang="en">Welcome</a>
    <a class="enter-button enter-button--french" href="#fr" lang="fr">Bienvenue</a>

    <footer class="photo-credit">
      <span class="photo-credit__rule"></span>
      <span class="photo-credit__dot"></span>
      <span class="photo-credit__text">Photo is courtesy of Gary Ostlund</span>
      <span class="photo-credit__dot"></span>
      <span class="photo-credit__rule"></span>
    </footer>
  </main>
</body>
</html>
```